New flavour! New packaging for Velocity Energy Drink!

We need a new packaging designed to show off our new grape flavored energy drink! It will require box design with matching sachets!

Established in 2018 we are a fully Australian owned and operated business that started out with 2 gamers that got sick and tired of sugary energy drinks OR expensive powder from the USA.

We are an energy drink in the esports and gaming space. Our new product is an energy drink in powder in boxes of 30 sachets (please see attached for product example)

Please see example 1 and 2 for our competitors product. We would ideally like to go a bit more minimalist than them but still have a great color pop on black backing.

Target Market(s)

Gamer's and esports athletes between the ages or 18-30

Font styles to use
Sans Serif
Other font styles liked:
• Helvetica

Colors
886aae
ffffff

Requirements
Must have
• Black base/background.
• Vibrant purple N in the Velocity Logo.
• Same or slightly different shades of purple for some text and highlights.
• Black, white and some shades of a vibrant purple (for the grape flavor)
• ingredients list (may need to be reformatted to suit)
• Please see attached for legislative requirements on the box and sachets.
Nice to have
• minimalist design but enough to be eye catching and somewhat playful
• Twitter: @VLCT_FUEL
• Instagram: @VLCT_FUEL
• Facebook: @VLCTFUEL
Should not have
• OTHER COLORS.
• Overly complex designs.

```html
<!DOCTYPE html>
<html lang="en">
<head>
<meta charset="utf-8">
<title>Velocity Energy Drink – Grape Flavour Sachet</title>
<link rel="stylesheet" href="https://fonts.googleapis.com/css2?family=Montserrat:ital,wght@0,400;0,600;0,800;0,900;1,800&display=swap">
<style>
  :root {
    --backdrop: #d4d4d4;
    --wrapper: #0d0d0f;
    --crimp: #3a1329;
    --crimp-shade: #24091a;
    --ink-light: #ffffff;
    --ink-soft: #d9d2e3;
    --grape: #a77fd6;
    --grape-brand: #886aae;
    --grape-light: #b79bcb;
    --grape-mid: #7a5aa6;
    --grape-deep: #4a2b6a;
  }
  * { margin: 0; padding: 0; box-sizing: border-box; }
  html, body { width: 1200px; height: 789px; overflow: hidden; }
  body {
    background: var(--backdrop);
    font-family: "Montserrat", "Helvetica", Arial, sans-serif;
    position: relative;
  }
  .sachet {
    position: absolute;
    left: 100px; top: 245px;
    width: 1000px; height: 300px;
  }
  .sachet__shape { position: absolute; inset: 0; width: 1000px; height: 300px; }
  .sachet__artwork {
    position: absolute;
    left: 580px; top: 26px;
    width: 340px; height: 250px;
    border-radius: 46% 54% 48% 52% / 55% 45% 55% 45%;
    background:
      radial-gradient(circle at 42% 46%, var(--grape-light) 0%, var(--grape-mid) 30%, var(--grape-deep) 58%, rgba(74,43,106,0.45) 78%, rgba(13,13,15,0) 100%);
  }
  .brand {
    position: absolute;
    left: 100px; top: 44px;
    display: flex;
    align-items: flex-start;
    gap: 14px;
  }
  .brand__mark {
    width: 18px; height: 18px;
    margin-top: 14px;
    background: var(--grape);
  }
  .brand__name {
    font-weight: 900;
    font-size: 78px;
    line-height: 1;
    letter-spacing: -1px;
    color: var(--ink-light);
    text-transform: uppercase;
  }
  .brand__descriptor {
    display: block;
    text-align: right;
    font-weight: 600;
    font-size: 13px;
    letter-spacing: 5px;
    color: var(--ink-light);
    text-transform: uppercase;
    margin-top: 6px;
  }
  .flavour {
    position: absolute;
    left: 100px; top: 160px;
    font-weight: 800;
    font-size: 30px;
    letter-spacing: 7px;
    color: var(--grape);
    text-transform: uppercase;
  }
  .ingredients-note {
    position: absolute;
    left: 100px; top: 212px;
    font-weight: 400;
    font-size: 14px;
    letter-spacing: 5px;
    color: var(--ink-soft);
    text-transform: uppercase;
  }
  .tagline {
    position: absolute;
    left: 100px; top: 236px;
    font-weight: 800;
    font-style: italic;
    font-size: 17px;
    letter-spacing: 3px;
    color: var(--grape-brand);
    text-transform: uppercase;
  }
</style>
</head>
<body>
  <div class="sachet">
    <svg class="sachet__shape" viewBox="0 0 1000 300" aria-hidden="true">
      <rect class="sachet__body" x="60" y="0" width="880" height="300" fill="var(--wrapper)"/>
      <path class="sachet__crimp sachet__crimp--left" fill="var(--crimp)"
        d="M60 0 H8 l-8 7.5 l8 7.5 l-8 7.5 l8 7.5 l-8 7.5 l8 7.5 l-8 7.5 l8 7.5 l-8 7.5 l8 7.5 l-8 7.5 l8 7.5 l-8 7.5 l8 7.5 l-8 7.5 l8 7.5 l-8 7.5 l8 7.5 l-8 7.5 l8 7.5 l-8 7.5 l8 7.5 l-8 7.5 l8 7.5 l-8 7.5 l8 7.5 l-8 7.5 l8 7.5 l-8 7.5 l8 7.5 l-8 7.5 l8 7.5 l-8 7.5 l8 7.5 l-8 7.5 l8 7.5 l-8 7.5 l8 7.5 l-8 7.5 l8 7.5 H60 Z"/>
      <path class="sachet__crimp sachet__crimp--right" fill="var(--crimp)"
        d="M940 0 H992 l8 7.5 l-8 7.5 l8 7.5 l-8 7.5 l8 7.5 l-8 7.5 l8 7.5 l-8 7.5 l8 7.5 l-8 7.5 l8 7.5 l-8 7.5 l8 7.5 l-8 7.5 l8 7.5 l-8 7.5 l8 7.5 l-8 7.5 l8 7.5 l-8 7.5 l8 7.5 l-8 7.5 l8 7.5 l-8 7.5 l8 7.5 l-8 7.5 l8 7.5 l-8 7.5 l8 7.5 l-8 7.5 l8 7.5 l-8 7.5 l8 7.5 l-8 7.5 l8 7.5 l-8 7.5 l8 7.5 l-8 7.5 l8 7.5 l-8 7.5 H940 Z"/>
      <rect x="56" y="0" width="6" height="300" fill="var(--crimp-shade)"/>
      <rect x="938" y="0" width="6" height="300" fill="var(--crimp-shade)"/>
    </svg>

    <div class="sachet__artwork" role="img" aria-label="Watercolour bunch of purple grapes on a lilac splash with a white running figure silhouette"></div>

    <div class="brand">
      <div>
        <div class="brand__name">Velocity</div>
        <span class="brand__descriptor">Energy Drink</span>
      </div>
      <span class="brand__mark" aria-hidden="true"></span>
    </div>
    <p class="flavour">Grape Flavour</p>
    <p class="ingredients-note">With Ginseng &amp; Caffeine</p>
    <p class="tagline">For Gamers, By Gamers</p>
  </div>
</body>
</html>
```